Pembrook Insurance Post Card

Specializing in “Towing & Transportation Insurance”
See our website at http://pembrookins-example.net/ for ideas on colors fonts etc.

Target Market(s)

Towing Companies

Font styles to use
Serif
Sans Serif

Requirements
Must have
• Specializing in “Towing & Transportation Insurance”
• Welcome to Pembrook Insurance:
• 2nd sentence (With our Agency, we work to make ourselves available to your business for when you need us most to keep your business moving forward.)
• 3rd Sentence: (Our customers were in mind when developing our agency and will continue to find new ways to make doing business with us easier.)
• We Offer: Change “Dealers Physical Damage” to “Auto Dealer Liability” & “Garage Liability” to “Garage Repair Liability”
• Our address: 718 Hollis Row NW, Suite F Decatur, AL 35988
• Email Address: PembrookInfo@velmarlink.example

```html
<!DOCTYPE html>
<html lang="en">
<head>
<meta charset="utf-8">
<title>Pembrook Insurance Post Card</title>
<link rel="stylesheet" href="https://fonts.googleapis.com/css2?family=Roboto+Condensed:ital,wght@0,400;0,700;1,300;1,400;1,700&family=Open+Sans:wght@600;700&display=swap">
<style>
:root{
  --navy:#0e2a43;
  --navy-deep:#0a1f33;
  --navy-light:#17405f;
  --gold:#9a6a14;
  --gold-soft:#e7c178;
  --white:#ffffff;
  --ink:#1b2a3a;
  --bg:#e6e6e6;
}
*{margin:0;padding:0;box-sizing:border-box}
html,body{width:879px;height:1200px;overflow:hidden;background:var(--bg)}
body{position:relative;font-family:"Roboto Condensed",sans-serif}
.card{position:absolute;left:98px;width:683px;height:487px;overflow:hidden;box-shadow:0 4px 14px rgba(0,0,0,.25)}
.card--front{top:70px;background:var(--navy)}
.card--back{top:651px;background:var(--white)}
.layer{position:absolute;left:0;top:0}

/* front */
.top-band{position:absolute;left:0;top:0;width:683px;height:73px;background:linear-gradient(90deg,var(--navy-deep),var(--navy-light))}
.photo{position:absolute;left:0;top:76px;width:683px;height:341px;background:linear-gradient(160deg,#8a6a5c 0%,#b9aea4 30%,#4d5d7a 55%,#2a3347 80%,#1c2230 100%)}
.gold-rule{position:absolute;left:0;height:4px;width:683px;background:var(--gold)}
.headline{position:absolute;left:18px;top:326px;color:var(--white);font-style:italic;font-weight:700;font-size:25px;line-height:27px;text-transform:uppercase;text-shadow:0 1px 3px rgba(0,0,0,.6)}
.brand{position:absolute;color:var(--navy);font-family:"Roboto Condensed",sans-serif;font-weight:700;text-align:center;text-transform:uppercase}
.brand__name{display:block;font-size:36px;letter-spacing:3px;line-height:38px}
.brand__sub{display:block;font-size:13px;letter-spacing:12px;line-height:16px;margin-right:-12px}
.offer-title{position:absolute;left:417px;width:255px;top:130px;text-align:center;color:var(--gold);font-weight:700;font-size:32px;line-height:38px}
.offer-list{position:absolute;list-style:none;font-size:13.5px;line-height:16px;color:var(--ink)}
.offer-list li{position:relative;padding-left:13px;margin-bottom:11px}
.offer-list li::before{content:"";position:absolute;left:0;top:5px;width:6px;height:6px;border-radius:50%;border:2px solid var(--gold)}
.contact-bar{position:absolute;left:18px;top:421px;height:66px;display:flex;align-items:center;color:var(--white);font-family:"Open Sans",sans-serif}
.contact-bar__cta{font-weight:600;font-size:20px;margin-right:24px}
.contact-bar__item{display:flex;align-items:center;font-weight:700;font-size:16px;gap:6px}
.contact-bar__sep{width:1px;height:20px;background:var(--white);margin:0 20px}
.social-dot{position:absolute;left:627px;top:443px;width:22px;height:22px;border-radius:50%;background:var(--navy-light)}

/* back */
.back-copy{position:absolute;left:18px;color:var(--white);font-style:italic;font-weight:700;font-size:14px;line-height:20px}
.quote{position:absolute;left:43px;top:279px;width:292px;color:var(--gold-soft);font-style:italic;font-weight:300;font-size:10.5px;line-height:20px;letter-spacing:-.1px}
.quote-mark{color:#8d98a4;font-family:Georgia,serif;font-weight:700}
.quote-mark--open{position:absolute;left:20px;top:268px;font-size:34px;line-height:34px}
.quote-mark--close{font-size:22px;line-height:10px;vertical-align:-8px;margin-left:8px}
.attribution{position:absolute;left:200px;width:131px;top:381px;text-align:right;color:var(--gold-soft);font-style:italic;font-weight:700;font-size:11px;line-height:12.5px}
.footer-line{position:absolute;left:14px;color:var(--white);font-size:10.5px;display:flex;align-items:center;gap:4px;white-space:nowrap}
.footer-line .sep{width:1px;height:12px;background:var(--white);margin:0 4px}
.stamp-box{position:absolute;left:584px;top:26px;width:72px;height:72px;border:1px solid #8b8b8b}
.address-line{position:absolute;left:451px;width:204px;height:1px;background:#9a9a9a}
.welcome{position:absolute;left:460px;width:182px;top:415px;text-align:center;color:var(--gold);font-weight:700;font-size:19px;line-height:22px}
</style>
</head>
<body>

<section class="card card--front">
  <div class="top-band"></div>
  <div class="gold-rule" style="top:73px;width:420px"></div>
  <div class="photo" role="img" aria-label="Photo of a damaged blue sedan loaded on a flatbed tow truck in front of brick houses"></div>
  <div class="gold-rule" style="top:417px"></div>
  <p class="headline">Specializing in<br>Towing &amp; Transportation<br>Insurance</p>

  <svg class="layer" width="683" height="487" viewBox="0 0 683 487" aria-hidden="true">
    <path d="M402 29 H683 V111 H402 A41 41 0 0 1 402 29 Z" fill="var(--white)"/>
    <polygon points="417,111 672,111 672,401 544,425 417,401" fill="var(--white)"/>
    <path d="M437 176 H538 L544 182 L550 176 H651" stroke="var(--navy)" stroke-width="1.5" fill="none"/>
  </svg>

  <div class="brand" style="left:420px;top:42px;width:230px">
    <span class="brand__name">Pembrook</span>
    <span class="brand__sub">Insurance</span>
  </div>

  <h2 class="offer-title">WE OFFER</h2>
  <ul class="offer-list" style="left:440px;top:200px;width:120px">
    <li>Auto Liability</li>
    <li>General Liability</li>
    <li>Garage Repair<br>Liability</li>
    <li>Garagekeepers</li>
    <li>Auto Dealer<br>Liability</li>
    <li>OnHook</li>
  </ul>
  <ul class="offer-list" style="left:556px;top:200px;width:115px">
    <li>Cargo</li>
    <li>Property</li>
    <li>Wrongful<br>Repossession</li>
    <li>Umbrella/Excess</li>
    <li>Workers<br>Compensation</li>
  </ul>

  <div class="contact-bar">
    <span class="contact-bar__cta">Call Now!</span>
    <span class="contact-bar__item">
      <svg width="13" height="13" viewBox="0 0 24 24" aria-hidden="true"><path d="M6.6 10.8a15 15 0 0 0 6.6 6.6l2.2-2.2c.3-.3.7-.4 1-.2 1.1.4 2.3.6 3.6.6.6 0 1 .4 1 1V20c0 .6-.4 1-1 1A17 17 0 0 1 3 4c0-.6.4-1 1-1h3.5c.6 0 1 .4 1 1 0 1.3.2 2.5.6 3.6.1.3 0 .7-.2 1z" fill="var(--white)"/></svg>
      +334-555-0187
    </span>
    <span class="contact-bar__sep"></span>
    <span class="contact-bar__item" style="font-size:15px">
      <svg width="14" height="14" viewBox="0 0 24 24" aria-hidden="true"><g fill="none" stroke="var(--white)" stroke-width="1.8"><circle cx="12" cy="12" r="10"/><ellipse cx="12" cy="12" rx="4.5" ry="10"/><path d="M2 12h20M4 7h16M4 17h16"/></g></svg>
      pembrookins-example.net
    </span>
  </div>
  <div class="social-dot"></div>
</section>

<section class="card card--back">
  <svg class="layer" width="683" height="487" viewBox="0 0 683 487" aria-hidden="true">
    <defs>
      <linearGradient id="headBand" x1="0" x2="1" y1="0" y2="0">
        <stop offset="0" stop-color="var(--navy)"/>
        <stop offset="1" stop-color="var(--navy-light)"/>
      </linearGradient>
    </defs>
    <polygon points="0,96 374,96 341,243 425,487 0,487" fill="var(--navy-deep)"/>
    <polygon points="0,96 374,96 355,179 0,179" fill="url(#headBand)"/>
    <polygon points="0,414 400,414 425,487 0,487" fill="var(--navy)"/>
    <polyline points="424,0 341,243 425,487" fill="none" stroke="var(--gold)" stroke-width="5"/>
  </svg>

  <div class="brand" style="left:18px;top:24px;width:215px">
    <span class="brand__name" style="font-size:34px">Pembrook</span>
    <span class="brand__sub">Insurance</span>
  </div>

  <p class="back-copy" style="top:108px;width:330px">With our Agency, we work to make ourselves available to your business for when you need us most to keep your business moving forward.</p>
  <p class="back-copy" style="top:198px;width:305px">Our customers were in mind when developing our agency and will continue to find new ways to make doing business with us easier.</p>

  <span class="quote-mark quote-mark--open">&ldquo;</span>
  <p class="quote">We have been very pleased with Pembrook Insurance. We have been in the trucking business for over 25 years and have found Pembrook to be one of the most thorough, hands on, dependable insurance agencies we have ever delt with. They are a caring company that keeps their clients first. Cudos to Pembrook, the best ever!<span class="quote-mark quote-mark--close">&rdquo;</span></p>
  <p class="attribution">Dale Horvath<br>Auto Transporter</p>

  <p class="footer-line" style="top:432px">
    <svg width="9" height="12" viewBox="0 0 12 16" aria-hidden="true"><path d="M6 0a6 6 0 0 0-6 6c0 4.5 6 10 6 10s6-5.5 6-10a6 6 0 0 0-6-6zm0 8.5A2.5 2.5 0 1 1 6 3.5a2.5 2.5 0 0 1 0 5z" fill="var(--white)"/></svg>
    Pembrook Insurance, LLC, 718 Hollis Row NW, Suite F Decatur, AL 35988
  </p>
  <p class="footer-line" style="top:456px;font-size:10px">
    <svg width="10" height="10" viewBox="0 0 24 24" aria-hidden="true"><path d="M6.6 10.8a15 15 0 0 0 6.6 6.6l2.2-2.2c.3-.3.7-.4 1-.2 1.1.4 2.3.6 3.6.6.6 0 1 .4 1 1V20c0 .6-.4 1-1 1A17 17 0 0 1 3 4c0-.6.4-1 1-1h3.5c.6 0 1 .4 1 1 0 1.3.2 2.5.6 3.6.1.3 0 .7-.2 1z" fill="var(--white)"/></svg>
    +334-555-0187
    <span class="sep"></span>
    <svg width="11" height="8" viewBox="0 0 22 16" aria-hidden="true"><rect x="1" y="1" width="20" height="14" fill="none" stroke="var(--white)" stroke-width="2"/><path d="M1 1l10 8 10-8" fill="none" stroke="var(--white)" stroke-width="2"/></svg>
    PembrookInfo@velmarlink.example
    <span class="sep"></span>
    <svg width="10" height="10" viewBox="0 0 24 24" aria-hidden="true"><g fill="none" stroke="var(--white)" stroke-width="2"><circle cx="12" cy="12" r="10"/><ellipse cx="12" cy="12" rx="4.5" ry="10"/><path d="M2 12h20"/></g></svg>
    pembrookins-example.net
  </p>

  <div class="stamp-box"></div>
  <div class="address-line" style="top:215px"></div>
  <div class="address-line" style="top:255px"></div>
  <div class="address-line" style="top:295px"></div>
  <div class="address-line" style="top:334px"></div>
  <p class="welcome">Welcome to<br>Pembrook Insurance</p>
</section>

</body>
</html>
```